I need a business card design for my new clinic (ATHLETIC CARE OF JOINT). I am orthopedist, expert in sports surgery, especially knee surgery. I prefer, as colors, the colors of my logo (green, black and white). I already have my logo and should appear on my card. It's good to see my site to have ideas (www.drlucianovarela.example)
It needs contain:
my name: Dr. Luciano Varela
my registration: CRM 584-902
my specialty: Cirurgia do Joelho / Esporte
my address: Centro Empresarial - Parque Aurora Mall
Av. Doutor Augusto Valadares Pinto, 2740 sala 803
Jd. Acácias - Ribeirão Preto - SP
my phone number: Tel (16) 8420-5937
my clinic phone: (16) 3745-8081
my e-mail: drlucianovarela@mailbox.example
my site: www.drlucianovarela.example

Target Market(s)

futures patients

Industry/Entity Type

Clinic

Requirements
Nice to have
• letters not overfilled
straight lines, with few curves

```html
<!DOCTYPE html>
<html lang="pt">
<head>
<meta charset="utf-8">
<title>Dr. Luciano Varela – Business Card</title>
<link href="https://fonts.googleapis.com/css2?family=Arimo:wght@400;700&family=Libre+Baskerville:wght@700&display=swap" rel="stylesheet">
<style>
  :root {
    --stage: #3a3a3a;
    --card-dark: #141210;
    --card-light: #f7f7f7;
    --green: #1f9a4e;
    --green-bright: #2fb865;
    --ink: #1a1a1a;
    --ink-soft: #2c2c2c;
    --white: #f2f2f2;
    --photo-warm: #b5651f;
    --photo-red: #9c2a1a;
  }
  * { box-sizing: border-box; margin: 0; padding: 0; }
  html, body { width: 1200px; height: 880px; overflow: hidden; }
  body {
    background: var(--stage);
    font-family: "Arimo", Arial, sans-serif;
    position: relative;
  }
  .card {
    position: absolute;
    left: 320px;
    width: 560px;
    height: 320px;
    border-radius: 22px;
    overflow: hidden;
  }

  /* Front: website side */
  .card--front { top: 60px; background: var(--card-dark); }
  .front__visual {
    position: absolute; inset: 0;
    background:
      radial-gradient(ellipse 55% 35% at 45% 12%, var(--photo-red) 0%, transparent 70%),
      radial-gradient(ellipse 60% 45% at 40% 65%, var(--photo-warm) 0%, rgba(120,60,20,.5) 45%, transparent 80%),
      linear-gradient(90deg, #0e0c0b 0%, #241a12 40%, #1a1410 70%, #0e0c0b 100%);
    opacity: .85;
  }
  .front__site {
    position: absolute;
    left: 36px; right: 36px; top: 118px;
    display: flex; align-items: baseline; justify-content: space-between;
    color: var(--white);
    letter-spacing: .25em;
    font-size: 16px;
    white-space: nowrap;
  }
  .front__site-name {
    color: var(--green-bright);
    font-size: 24px;
    letter-spacing: .12em;
    position: relative; top: 22px;
  }

  /* Back: contact side */
  .card--back { top: 500px; background: var(--card-light); color: var(--ink); }
  .brand {
    position: absolute; left: 34px; top: 28px;
    display: flex; align-items: center; gap: 12px;
  }
  .brand__square { width: 44px; height: 44px; background: var(--ink); }
  .brand__name {
    font-family: "Libre Baskerville", Georgia, serif;
    font-weight: 700; font-size: 40px; color: var(--ink);
    letter-spacing: .02em;
  }
  .brand__decor {
    position: absolute; right: 40px; top: 64px;
    width: 120px; height: 120px;
    border-radius: 18px;
    background: #ecefed;
    border: 2px solid #e2e6e4;
  }
  .doctor { position: absolute; left: 40px; top: 104px; }
  .doctor__name { color: var(--green); font-size: 22px; font-weight: 400; }
  .doctor__spec, .doctor__crm { font-size: 13px; color: var(--ink-soft); margin-top: 5px; }
  .contact {
    position: absolute; left: 40px; top: 196px;
    display: grid; grid-template-columns: 82px auto;
    row-gap: 2px; column-gap: 6px;
    font-size: 13px; color: var(--ink-soft);
  }
  .contact dt { font-size: 11.5px; padding-top: 1px; }
  .contact dd { font-size: 13px; }
</style>
</head>
<body>

<section class="card card--front">
  <div class="front__visual" role="img" aria-label="Photograph of an athlete's leg in motion overlaid with a biomechanical line drawing of the knee joint"></div>
  <p class="front__site"><span>www.</span><span class="front__site-name">DRLUCIANOVARELA</span><span>.example</span></p>
</section>

<section class="card card--back">
  <div class="brand">
    <span class="brand__square"></span>
    <span class="brand__name">VARELA</span>
  </div>
  <div class="brand__decor" aria-hidden="true"></div>

  <div class="doctor">
    <h1 class="doctor__name">Dr. Luciano Varela</h1>
    <p class="doctor__spec">Cirurgia do Joelho / Esporte</p>
    <p class="doctor__crm">CRM 584-902</p>
  </div>

  <dl class="contact">
    <dt>Phone:</dt><dd>(16) 8420-5937</dd>
    <dt>Clinic Phone:</dt><dd>(16) 3745-8081</dd>
    <dt>Email:</dt><dd>drlucianovarela@mailbox.example</dd>
    <dt>Adress:</dt><dd>Centro Empresarial - Parque Aurora Mall<br>Av. Doutor Augusto Valadares Pinto, 2740 sala 803</dd>
  </dl>
</section>

</body>
</html>
```